Thriller/Romance novel book cover design - Eight Grey Gulls

I need a book cover for a novel (print + ebook). Genre = thriller / romance. Title = Eight Grey Gulls. Author = Dorian Felt.
Story is set in Caribbean. 45-year-old Ex-NVB agent is hunted by corrupt politicians, NVB and cartel. He is a life-long fisherman and seaman who joined the Army after college and became a war hero, followed by 10 years as operative for the NVB. Betrayal from Washington saw him accused of killing his mentor/friend/NVB Director and he is now a fugitive. He has been hiding for 7 years on Grand Cayman, and lives a secluded, private life as a fisherman on his modern sportfisherman-style boat ('50 Quellmoor Runabout for reference). Boat name = Eight Grey Gulls (as in the playing card) represents fate to him and his high school sweetheart to whom he was engaged before a tragic event separated them. His main goal, beyond survival, is to reunite with his long, lost love, but he can't risk putting her in danger until he settles the case and those searching for him. The boat name (Eight Grey Gulls) only has relevance to him and his soulmate, who is not even aware that he is still alive.

Target Market(s)

thriller and romantic thriller readers

Requirements
Must have
• author name should be small on bottom of cover - not at top. Design is wide open for creative ideas. If a boat is used in artwork, it must be a modern sportfisherman style boat (zintrope will define this
Nice to have
• I like intrigue and mystery. Don't try to explain or show too much. Prefer sunsets (orange, red, purple, yellow) to blue sky, blue water to give it a darker tone
Should not have
• do not want images of people on the cover like many romance novels do.

```html
<!DOCTYPE html>
<html lang="en">
<head>
<meta charset="utf-8">
<title>Eight Grey Gulls — Cover Spread</title>
<link rel="stylesheet" href="https://fonts.googleapis.com/css2?family=Abril+Fatface&family=Playfair+Display:ital@1&family=Lato:ital,wght@0,400;1,400&family=Josefin+Sans:wght@400&display=swap">
<style>
  :root {
    --page: #ffffff;
    --sky-deep: #14264f;
    --sky-mid: #2c3f78;
    --dusk-violet: #6a4a86;
    --sunset-red: #d7402c;
    --sunset-orange: #f08a2a;
    --sunset-gold: #f7c54a;
    --sea-deep: #0c1a3c;
    --sea-mid: #1f2e5e;
    --hull-light: #c9cedb;
    --hull-mid: #5d6684;
    --hull-dark: #1a2140;
    --title-cream: #f7ebe6;
    --blurb-text: #f2f2f4;
    --author-teal: #a9d6cc;
    --barcode-box: #ffffff;
  }
  * { margin: 0; padding: 0; box-sizing: border-box; }
  html, body {
    width: 1200px; height: 1200px; overflow: hidden;
    background: var(--page);
  }
  .canvas { position: relative; width: 1200px; height: 1200px; }

  .spread {
    position: absolute; left: 40px; top: 197px;
    width: 1120px; height: 806px; overflow: hidden;
  }
  .spread-art {
    position: absolute; inset: 0;
    background:
      radial-gradient(ellipse 460px 130px at 820px 388px, rgba(247,197,74,0.95), rgba(240,138,42,0.7) 45%, rgba(215,64,44,0) 100%),
      linear-gradient(to bottom,
        var(--sky-deep) 0px,
        var(--sky-mid) 110px,
        var(--dusk-violet) 210px,
        var(--sunset-red) 300px,
        var(--sunset-orange) 360px,
        var(--sunset-gold) 385px,
        var(--sunset-orange) 400px,
        #b4442f 440px,
        var(--sea-mid) 540px,
        var(--sea-deep) 806px);
  }
  .back-shade {
    position: absolute; left: 0; top: 0; width: 560px; height: 806px;
    background: linear-gradient(to right, rgba(12,26,60,0.85) 0%, rgba(20,38,79,0.6) 70%, rgba(20,38,79,0) 100%);
  }
  .boat-art {
    position: absolute; left: 712px; top: 222px; width: 298px; height: 386px;
    border-radius: 14px 14px 24px 24px;
    background: linear-gradient(to bottom,
      var(--hull-dark) 0%,
      var(--hull-mid) 45%,
      var(--hull-light) 62%,
      var(--hull-mid) 80%,
      var(--hull-dark) 100%);
    box-shadow: 0 20px 40px rgba(8,14,34,0.6);
  }

  /* Back cover */
  .blurb {
    position: absolute; left: 33px; top: 110px; width: 318px;
    font-family: "Lato", sans-serif; color: var(--blurb-text);
    font-size: 15px; line-height: 22.5px;
  }
  .blurb-lead {
    font-style: italic; font-size: 18.5px; line-height: 24px;
    margin-bottom: 25px;
  }
  .blurb p + p { margin-top: 22px; }
  .blurb em { font-style: italic; }

  .barcode-area {
    position: absolute; left: 337px; top: 673px;
    width: 179px; height: 100px; border-radius: 14px;
    background: var(--barcode-box);
  }

  /* Spine */
  .spine-title, .spine-author {
    position: absolute; writing-mode: vertical-rl;
    color: var(--title-cream); white-space: nowrap;
  }
  .spine-title {
    left: 538px; top: 34px; font-family: "Abril Fatface", serif; font-size: 40px;
    line-height: 44px;
  }
  .spine-title .connector { font-family: "Playfair Display", serif; font-style: italic; font-size: 30px; }
  .spine-author {
    top: 650px; left: 542px; font-family: "Josefin Sans", sans-serif;
    font-size: 34px; line-height: 38px; letter-spacing: 3px; color: var(--blurb-text);
  }

  /* Front cover */
  .front-title {
    position: absolute; left: 640px; top: 0; width: 460px; height: 260px;
    color: var(--title-cream); opacity: 0.95; font-weight: normal;
  }
  .front-title span { position: absolute; left: 0; width: 100%; text-align: center; }
  .front-title .word {
    font-family: "Abril Fatface", serif;
    font-size: 112px; line-height: 112px; letter-spacing: 4px;
  }
  .front-title .word-top { top: 12px; }
  .front-title .word-bottom { top: 136px; }
  .front-title .connector {
    top: 92px; font-family: "Playfair Display", serif; font-style: italic;
    font-size: 58px; line-height: 60px; padding-left: 10px;
  }
  .author {
    position: absolute; left: 660px; top: 733px; width: 380px;
    text-align: center; font-family: "Josefin Sans", sans-serif;
    font-size: 47px; letter-spacing: 2px; color: var(--author-teal);
    white-space: nowrap;
  }
</style>
</head>
<body>
<main class="canvas">
  <section class="spread">
    <div class="spread-art" role="img" aria-label="Caribbean sunset over dark sea with a wooded shoreline on the back cover"></div>
    <div class="back-shade"></div>
    <div class="boat-art" role="img" aria-label="Photo of a modern sportfisherman boat seen from the stern with lit cockpit and tall tuna tower, heading into the sunset"></div>

    <div class="blurb">
      <p class="blurb-lead">The story is set in the Caribbean...</p>
      <p>A 45-year-old ex-NVB agent is hunted by corrupt politicians, NVB and cartel. He is a life-long fisherman and seaman who joined the Army after college and became a war hero, followed by 10 years as an operative for the NVB. Betrayal from Washington saw him accused of killing his mentor/friend/ NVB Director and he is now a fugitive.</p>
      <p>He has been hiding for 7 years on Grand Cayman, and lives a secluded, private life as a fisherman on his modern sportfisherman-style boat, called Eight Grey Gulls. It represents fate to him and his high school sweetheart to whom he was engaged before a tragic event separated them. His main goal, beyond survival, is to reunite with his long, lost love, but he can't risk putting her in danger until he settles the case and those searching for him. The boat name only has relevance to him and his soulmate, <em>who is not even aware that he is still alive.</em></p>
    </div>
    <div class="barcode-area"></div>

    <div class="spine-title">Eight <span class="connector">Grey</span> Gulls</div>
    <div class="spine-author">FELT</div>

    <h1 class="front-title">
      <span class="word word-top">Eight</span>
      <span class="connector">Grey</span>
      <span class="word word-bottom">Gulls</span>
    </h1>
    <p class="author">DORIAN FELT</p>
  </section>
</main>
</body>
</html>
```